Velmoxa AdAgency Presentation

We need ppt design for an ad agency re-branding, agency is based in Moscow, Russia. Our specifics is brand audit, consulting and strategy in web and offline.
We decided to do re-branding because our current agency does not answer the purpose and we need a kind of "second breath".
The idea of re-branding appeared because of many changes that happened in company: new clients, new projects level, new team.
So we'd like to promote company of changes and design should show this spirit as possible.
You may use info in attached pdf file (sorry for Russian language). Info is not so necessary, it will be replaced later.

Please use more colors than digital blue and grey!

Industry/Entity Type

Ad Agency

Requirements
Must have
• Logo is attached. Please choose one.

Ppt project should include:
- Front and last page design
- Heading and list design
- Page-separator design
- Diagram design
- Pics appearance

```html
<!DOCTYPE html>
<html lang="en">
<head>
<meta charset="utf-8">
<title>Velmoxa Agency Presentation</title>
<link href="https://fonts.googleapis.com/css2?family=Open+Sans:wght@300;400;600;700&display=swap" rel="stylesheet">
<style>
:root{
  --night:#0d0d0e;
  --ocean:#1f5f85;
  --ocean-deep:#154764;
  --accent:#3b62b3;
  --teal:#1fa89a;
  --amber:#f4a32b;
  --coral:#e8603c;
  --leaf:#78b83a;
  --sun:#f2e22a;
  --paper-edge:#c9c0b5;
  --ink:#333;
  --table-head:#4a6fb0;
  --table-row:#dde4f0;
  --table-alt:#c8d4ea;
}
*{box-sizing:border-box;margin:0;padding:0}
html,body{width:1200px;height:1164px;overflow:hidden;background:var(--night)}
body{position:relative;font-family:"Open Sans",Arial,sans-serif;color:var(--ink)}
.slide{position:absolute;width:279px;height:209px;overflow:hidden}
.c1{left:22px}.c2{left:314px}.c3{left:607px}.c4{left:899px}
.r1{top:22px}.r2{top:249px}.r3{top:477px}.r4{top:704px}.r5{top:932px}

.content{background:radial-gradient(ellipse at 50% 42%,#f3efea 0%,#e5dfd7 55%,var(--paper-edge) 100%)}
.content::before{content:"";position:absolute;left:10px;top:0;width:96px;height:3px;
  background:linear-gradient(90deg,var(--accent) 0 25%,var(--teal) 25% 50%,var(--amber) 50% 75%,var(--coral) 75% 100%)}
.slide-head{position:absolute;left:14px;top:19px;font-size:5.4px;font-weight:300;letter-spacing:.3px;color:#7a7a7a;text-transform:uppercase;white-space:nowrap}
.brand-mark{position:absolute;right:12px;top:8px;display:flex;flex-direction:column;align-items:center;gap:1px}
.brand-mark .square{width:10px;height:10px;background:#5d5d5d}
.brand-mark .name{font-size:3.8px;color:#5d5d5d}
.slide-foot{position:absolute;left:14px;right:14px;bottom:7px;display:flex;justify-content:space-between;font-size:3.4px;color:#8a8a8a}

.copy{font-size:3.6px;line-height:1.38;color:var(--ink);text-align:justify}
.copy p+p{margin-top:3px}
.abs{position:absolute}
.photo{position:absolute}

.title-slide{background:linear-gradient(180deg,#6d8da6 0%,#4f7594 45%,#2d6388 70%,var(--ocean-deep) 100%)}
.title-slide .backdrop{position:absolute;inset:0;background:linear-gradient(90deg,rgba(255,255,255,.05),rgba(255,255,255,.18) 40%,rgba(255,255,255,.04))}
.title-slide .lower-band{position:absolute;left:0;right:0;top:155px;height:40px;background:linear-gradient(180deg,#2a6b93,#1d5a80)}
.light-brand{position:absolute;left:13px;top:14px;display:flex;flex-direction:column;gap:2px}
.light-brand .square{width:12px;height:12px;background:#fff}
.light-brand .name{font-size:5px;color:#fff}
.big-title{position:absolute;left:0;right:0;text-align:center;color:#fff;font-weight:300;font-size:14.5px;letter-spacing:.4px;white-space:nowrap}
.sub-title{position:absolute;left:0;right:0;text-align:center;color:var(--sun);font-weight:700;font-size:5.2px;white-space:nowrap}
.light-foot{position:absolute;right:10px;bottom:7px;font-size:3.4px;color:#dfe8f0}

.cover{background:radial-gradient(ellipse at 40% 35%,#2b7aa6 0%,var(--ocean) 55%,#154a6a 100%)}
.cover .light-brand{left:48px;top:98px;align-items:flex-start}
.cover .light-brand .square{width:16px;height:18px}
.cover .light-brand .name{font-size:8.5px}

.num{position:absolute;width:9px;height:9px;border-radius:50%;color:#fff;font-size:3.6px;font-weight:700;display:flex;align-items:center;justify-content:center}
.n1{background:var(--accent)}.n2{background:var(--teal)}.n3{background:var(--amber)}
.n4{background:var(--coral)}.n5{background:var(--leaf)}.n6{background:#6a5bb5}
.item-head{font-size:4.2px;font-weight:700;color:var(--ink);border-bottom:.5px solid #aaa;padding-bottom:1px;margin-bottom:1.5px}

.caption{font-size:3.6px;line-height:1.35;text-align:center;color:var(--ink)}
.caption b{display:block;font-weight:700}

.bullets{list-style:none;font-size:3.6px;line-height:2.05;color:var(--ink)}
.bullets li::before{content:"";display:inline-block;width:2.4px;height:2.4px;background:var(--teal);margin-right:4px;vertical-align:middle}

table.data{border-collapse:collapse;font-size:3.2px;color:#223}
table.data th{background:var(--table-head);color:#fff;font-weight:600;padding:1.5px 3px;text-align:left}
table.data td{padding:1.5px 3px;background:var(--table-row)}
table.data tr:nth-child(even) td{background:var(--table-alt)}
table.data tr td:first-child{background:var(--table-head);color:#fff}

.map-area{position:absolute;left:40px;top:60px;width:200px;height:110px;border-radius:6px;
  background:linear-gradient(160deg,#8fd3ef 0%,#6cc0e5 55%,#58b3dc 100%)}
.map-stat{position:absolute;font-size:4px;font-weight:700;color:#fff;padding:1px 3px;border-radius:4px}
.map-group{position:absolute;height:5px;border-radius:1px}

.section-slide{background:linear-gradient(180deg,#eef0f3 0%,#d7dde4 100%)}
.section-slide .band{position:absolute;left:0;right:0;top:58px;height:96px;background:linear-gradient(90deg,#2e5f8c,#4d7aa3 60%,#6f93b5)}
</style>
</head>
<body>

<section class="slide cover c1 r1">
  <div class="light-brand"><span class="square"></span><span class="name">Velmoxa</span></div>
  <div class="photo" role="img" aria-label="Screens of laptop, tablet and phones showing agency work" style="left:150px;top:48px;width:118px;height:122px;background:linear-gradient(160deg,#3a3f47 0%,#b8692e 45%,#f0f0f0 80%);border-radius:3px;opacity:.9"></div>
</section>

<section class="slide title-slide c2 r1">
  <div class="backdrop" role="img" aria-label="Faded city bridge backdrop"></div>
  <div class="lower-band"></div>
  <div class="light-brand"><span class="square"></span><span class="name">Velmoxa</span></div>
  <h1 class="big-title" style="top:100px">YOUR TITTLE HERE</h1>
  <p class="sub-title" style="top:122px">YOUR PRESENTATION SUB TITLE HERE</p>
  <p class="light-foot">© 2013 VELMOXA. All rights reserved</p>
</section>

<section class="slide content c3 r1">
  <p class="slide-head">Velmoxa presentation/powerful mission 1</p>
  <div class="brand-mark"><span class="square"></span><span class="name">Velmoxa</span></div>
  <div class="photo" role="img" aria-label="Office tower at night" style="left:24px;top:46px;width:70px;height:118px;background:linear-gradient(180deg,#1f2c4a 0%,#2f4a7a 50%,#caa35a 100%)"></div>
  <div class="copy abs" style="left:131px;top:56px;width:126px">
    <p>Velmoxa has built a bold and dynamic approach to brand audit and strategy. By clearing old habits that held the market back, the team has pushed clients to a new level.</p>
    <p>Central to this approach are fresh habits that help the brand move forward. Our team has pushed each project to a new level of audit and strategy work, growing brands across web and offline channels and bringing results to clients.</p>
  </div>
  <footer class="slide-foot"><span>© 2013 Velmoxa. All rights reserved</span><span>1</span></footer>
</section>

<section class="slide content c4 r1">
  <p class="slide-head">Velmoxa presentation/powerful mission 1</p>
  <div class="brand-mark"><span class="square"></span><span class="name">Velmoxa</span></div>
  <div class="photo" role="img" aria-label="Team of colleagues together" style="left:34px;top:49px;width:92px;height:42px;background:linear-gradient(90deg,#e8e4de,#b89a82 50%,#e5e1db)"></div>
  <div class="copy abs" style="left:34px;top:99px;width:92px"><p>Velmoxa has built a bold and dynamic approach to brand audit and consulting research.</p><p>By clearing old habits that held the market back, the team has pushed clients to a new level with each project.</p></div>
  <div class="copy abs" style="left:141px;top:49px;width:112px">
    <p>Velmoxa has built a bold and dynamic approach to brand audit and strategy. By clearing old habits that held the market back, the team has pushed clients to a new level.</p>
    <p>Central to this approach are fresh habits that help the brand move forward. Our team has pushed each project to a new level of audit and strategy work with these models.</p>
  </div>
  <footer class="slide-foot"><span>© 2013 Velmoxa. All rights reserved</span><span>2</span></footer>
</section>

<section class="slide content c1 r2">
  <p class="slide-head">Velmoxa presentation/powerful mission 1</p>
  <div class="brand-mark"><span class="square"></span><span class="name">Velmoxa</span></div>
  <span class="num n1" style="left:40px;top:70px">1.</span>
  <div class="abs" style="left:58px;top:67px;width:195px"><p class="item-head">We know firsthand 1</p><p class="copy">Since 1998, we have supported thousands of clients from the first brand audit through their full journey with the market.</p></div>
  <span class="num n2" style="left:40px;top:112px">2.</span>
  <div class="abs" style="left:58px;top:109px;width:195px"><p class="item-head">We know firsthand 2</p><p class="copy">Since 1998, we have supported thousands of clients from the first brand audit through their journey with the market, and we have guided thousands of clients from the first brief through launch.</p></div>
  <span class="num n3" style="left:40px;top:153px">3.</span>
  <div class="abs" style="left:58px;top:150px;width:195px"><p class="item-head">We know firsthand 3</p><p class="copy">Since 1998, we have supported thousands of clients from the first brand audit through their journey, and we have guided thousands of clients.</p></div>
  <footer class="slide-foot"><span>© 2013 Velmoxa. All rights reserved</span><span>3</span></footer>
</section>

<section class="slide content c2 r2">
  <p class="slide-head">Velmoxa presentation/powerful mission 1</p>
  <div class="brand-mark"><span class="square"></span><span class="name">Velmoxa</span></div>
  <span class="num n1" style="left:38px;top:63px">1.</span>
  <div class="abs" style="left:54px;top:60px;width:78px"><p class="item-head">We know firsthand 1</p><p class="copy">Since 1998, we have supported thousands of clients from the first audit through their journey.</p></div>
  <span class="num n2" style="left:38px;top:98px">2.</span>
  <div class="abs" style="left:54px;top:95px;width:78px"><p class="item-head">We know firsthand 1</p><p class="copy">Since 1998, we have supported thousands of clients from the first audit.</p></div>
  <span class="num n3" style="left:38px;top:129px">3.</span>
  <div class="abs" style="left:54px;top:126px;width:78px"><p class="item-head">We know firsthand 1</p><p class="copy">Since 1998, we have supported thousands of clients from the first audit through their journey.</p></div>
  <span class="num n4" style="left:142px;top:63px">4.</span>
  <div class="abs" style="left:158px;top:60px;width:78px"><p class="item-head">We know firsthand 1</p><p class="copy">Since 1998, we have supported thousands of clients from the first audit through their journey.</p></div>
  <span class="num n5" style="left:142px;top:98px">5.</span>
  <div class="abs" style="left:158px;top:95px;width:78px"><p class="item-head">We know firsthand 1</p><p class="copy">Since 1998, we have supported thousands of clients from the first audit.</p></div>
  <span class="num n6" style="left:142px;top:129px">6.</span>
  <div class="abs" style="left:158px;top:126px;width:78px"><p class="item-head">We know firsthand 1</p><p class="copy">Since 1998, we have supported thousands of clients from the first audit through their journey.</p></div>
  <footer class="slide-foot"><span>© 2013 Velmoxa. All rights reserved</span><span>3</span></footer>
</section>

<section class="slide content c3 r2">
  <p class="slide-head">Velmoxa presentation/powerful mission 1</p>
  <div class="brand-mark"><span class="square"></span><span class="name">Velmoxa</span></div>
  <div class="photo" role="img" aria-label="Laptop showing agency website" style="left:38px;top:66px;width:48px;height:32px;background:linear-gradient(180deg,#2a3140,#3f6d9c 60%,#9aa3ad)"></div>
  <div class="photo" role="img" aria-label="Laptop showing agency website" style="left:110px;top:66px;width:48px;height:32px;background:linear-gradient(180deg,#2a3140,#3f6d9c 60%,#9aa3ad)"></div>
  <div class="photo" role="img" aria-label="Laptop showing agency website" style="left:186px;top:66px;width:48px;height:32px;background:linear-gradient(180deg,#2a3140,#3f6d9c 60%,#9aa3ad)"></div>
  <p class="caption abs" style="left:28px;top:110px;width:68px"><b>Full Data in Moscow</b>a small team of fresh minds has worked with many local brands and helped them grow across web and print.</p>
  <p class="caption abs" style="left:100px;top:110px;width:68px"><b>Full Data in Moscow</b>a small team of fresh minds has worked with many local brands.</p>
  <p class="caption abs" style="left:176px;top:110px;width:68px"><b>Full Data in Moscow</b>a small team of fresh minds has worked with many local brands and print.</p>
  <footer class="slide-foot"><span>© 2013 Velmoxa. All rights reserved</span><span>3</span></footer>
</section>

<section class="slide content c4 r2">
  <p class="slide-head">Velmoxa presentation/powerful mission 1</p>
  <div class="brand-mark"><span class="square"></span><span class="name">Velmoxa</span></div>
  <div class="photo" role="img" aria-label="Desktop, tablet and phone screens showing projects" style="left:32px;top:68px;width:104px;height:88px;background:linear-gradient(150deg,#30343c 0%,#b86a34 45%,#f2f2f2 85%);border-radius:2px"></div>
  <div class="copy abs" style="left:151px;top:58px;width:104px">
    <p>Velmoxa has built a bold and dynamic approach to brand audit and strategy. By clearing old habits that held the market back, the team has pushed clients to a new level.</p>
    <p>Central to this approach are fresh habits that help the brand move forward. Our team has pushed each project to a new level of audit and strategy work with these models.</p>
  </div>
  <footer class="slide-foot"><span>© 2013 Velmoxa. All rights reserved</span><span>3</span></footer>
</section>

<section class="slide content c1 r3">
  <p class="slide-head">Velmoxa presentation/powerful mission 1</p>
  <div class="brand-mark"><span class="square"></span><span class="name">Velmoxa</span></div>
  <div class="photo" role="img" aria-label="Laptop showing agency website" style="left:38px;top:54px;width:36px;height:24px;background:linear-gradient(180deg,#2a3140,#3f6d9c 60%,#9aa3ad)"></div>
  <p class="copy abs" style="left:80px;top:56px;width:125px;text-align:left"><b>Full Data in Moscow</b><br>a small team of fresh minds has worked with many local brands and helped them grow across web and print.</p>
  <p class="copy abs" style="left:60px;top:102px;width:115px;text-align:right"><b>Full Data in Moscow</b><br>a small team of fresh minds has worked with many local brands.</p>
  <div class="photo" role="img" aria-label="Laptop showing agency website" style="left:182px;top:100px;width:36px;height:24px;background:linear-gradient(180deg,#2a3140,#3f6d9c 60%,#9aa3ad)"></div>
  <div class="photo" role="img" aria-label="Laptop showing agency website" style="left:38px;top:145px;width:36px;height:24px;background:linear-gradient(180deg,#2a3140,#3f6d9c 60%,#9aa3ad)"></div>
  <p class="copy abs" style="left:80px;top:147px;width:125px;text-align:left"><b>Full Data in Moscow</b><br>a small team of fresh minds has worked with many local brands and helped them grow across web and print.</p>
  <footer class="slide-foot"><span>© 2013 Velmoxa. All rights reserved</span><span>3</span></footer>
</section>

<section class="slide content c2 r3">
  <p class="slide-head">Velmoxa presentation/powerful mission 1</p>
  <div class="brand-mark"><span class="square"></span><span class="name">Velmoxa</span></div>
  <div class="map-area" role="img" aria-label="World map in light blue showing client share by region"></div>
  <span class="map-stat" style="left:72px;top:88px;background:var(--accent)">33%</span>
  <span class="map-stat" style="left:122px;top:90px;background:var(--teal)">31%</span>
  <span class="map-stat" style="left:182px;top:96px;background:var(--amber)">44%</span>
  <span class="map-stat" style="left:104px;top:128px;background:var(--coral)">24%</span>
  <span class="map-stat" style="left:200px;top:140px;background:var(--leaf)">8%</span>
  <span class="map-group" style="left:160px;top:50px;width:22px;background:#8a8a8a"></span>
  <span class="map-group" style="left:30px;top:118px;width:20px;height:10px;background:#8a8a8a"></span>
  <span class="map-group" style="left:56px;top:168px;width:20px;background:#8a8a8a"></span>
  <span class="map-group" style="left:106px;top:156px;width:14px;background:#8a8a8a"></span>
  <footer class="slide-foot"><span>© 2013 Velmoxa. All rights reserved</span><span>3</span></footer>
</section>

<section class="slide section-slide c3 r3">
  <div class="band"></div>
  <div class="abs" style="left:124px;top:18px;display:flex;flex-direction:column;align-items:center;gap:2px">
    <span style="width:11px;height:11px;background:#5b7fa6"></span><span style="font-size:4.5px;color:#5b7fa6">Velmoxa</span>
  </div>
  <h2 class="big-title" style="top:88px;left:44px;text-align:left">• YOUR TITTLE HERE</h2>
  <p class="sub-title" style="top:110px;left:78px;text-align:left">YOUR PRESENTATION SUB TITLE HERE</p>
  <p class="abs" style="left:12px;bottom:7px;font-size:3.4px;color:#7c8794">© 2013 VELMOXA. All rights reserved</p>
</section>

<section class="slide content c4 r3">
  <p class="slide-head">Velmoxa presentation/powerful mission 1</p>
  <div class="brand-mark"><span class="square"></span><span class="name">Velmoxa</span></div>
  <svg class="abs" style="left:22px;top:58px" width="236" height="52" viewBox="0 0 236 52">
    <g font-family="Open Sans, sans-serif" font-size="4" font-weight="700" fill="#fff" text-anchor="middle">
      <circle cx="212" cy="26" r="24" fill="#e8603c"/>
      <circle cx="165" cy="26" r="24" fill="#f4a32b"/>
      <circle cx="118" cy="26" r="24" fill="#1fa89a"/>
      <circle cx="71" cy="26" r="24" fill="#3677c0"/>
      <circle cx="24" cy="26" r="24" fill="#2b4f9c"/>
      <text x="24" y="27.5">BRIEF</text><text x="71" y="27.5">ANALYSIS</text><text x="118" y="27.5">DESIGN</text><text x="165" y="27.5">DEVELOP</text><text x="212" y="27.5">TESTING</text>
    </g>
  </svg>
  <div class="copy abs" style="left:40px;top:121px;width:200px">
    <p>Velmoxa has pushed each brand to a new level. The pace of change across our clients opens new work in audit, web and offline strategy that is brought to every partner.</p>
    <p>By clearing old habits that held the market back, Velmoxa has pushed each brand to a new level and turned fresh ideas into real results.</p>
  </div>
  <footer class="slide-foot"><span>© 2013 Velmoxa. All rights reserved</span><span>3</span></footer>
</section>

<section class="slide content c1 r4">
  <p class="slide-head">Velmoxa presentation/powerful mission 1</p>
  <div class="brand-mark"><span class="square"></span><span class="name">Velmoxa</span></div>
  <svg class="abs" style="left:14px;top:58px" width="112" height="116" viewBox="0 0 112 116">
    <g font-family="Open Sans, sans-serif" font-size="4.2" font-weight="700" fill="#fff" text-anchor="middle">
      <ellipse cx="56" cy="60" rx="54" ry="54" fill="#2b4f9c"/>
      <ellipse cx="56" cy="68" rx="45" ry="46" fill="#3677c0"/>
      <ellipse cx="56" cy="76" rx="37" ry="38" fill="#1fa89a"/>
      <ellipse cx="56" cy="84" rx="29" ry="30" fill="#f4a32b"/>
      <ellipse cx="56" cy="92" rx="21" ry="22" fill="#e8603c"/>
      <text x="56" y="14">BRIEF</text><text x="56" y="27">ANALYSIS</text><text x="56" y="44">DESIGN</text><text x="56" y="60">DEVELOP</text><text x="56" y="80">TESTING</text>
    </g>
  </svg>
  <ul class="bullets abs" style="left:142px;top:60px;width:115px">
    <li>Since 1998, we have supported</li><li>Central to this approach remains</li><li>Habits that held the industry</li><li>Since 1998, we have supported</li><li>Central to this approach remains</li><li>Habits that held the market</li><li>Fresh ideas that help brands</li><li>Many local brands in the city</li><li>Since 1998, we have supported</li><li>Central to this approach remains</li><li>Habits that held the industry</li>
  </ul>
  <footer class="slide-foot"><span>© 2013 Velmoxa. All rights reserved</span><span>3</span></footer>
</section>

<section class="slide content c2 r4">
  <p class="slide-head">Velmoxa presentation/powerful mission 1</p>
  <div class="brand-mark"><span class="square"></span><span class="name">Velmoxa</span></div>
  <div class="copy abs" style="left:26px;top:58px;width:92px">
    <p>Velmoxa has built a bold and dynamic approach to brand audit and strategy. By clearing old habits, the team has pushed clients to a new level.</p>
    <p>Central to this approach are fresh habits that held the market back. Velmoxa has pushed each project to a new level with new work in audit and strategy. Our partners grow across web and offline channels, and the pace of change is brought to every client.</p>
  </div>
  <svg class="abs" style="left:128px;top:72px" width="128" height="90" viewBox="0 0 100 70">
    <path d="M10 30 L10 38 A40 18 0 0 0 90 38 L90 30 A40 18 0 0 1 10 30 Z" fill="#1d4f8c"/>
    <path d="M50 30 L70 14.4 A40 18 0 1 1 10 30 Z" fill="#2a78c8"/>
    <path d="M50 30 L10 30 A40 18 0 0 1 50 12 Z" fill="#f4a32b"/>
    <path d="M50 30 L50 12 A40 18 0 0 1 70 14.4 Z" fill="#1fa89a"/>
    <g font-family="Open Sans, sans-serif" font-size="2.4" fill="#666">
      <text x="10" y="64"><tspan fill="#2a78c8">■</tspan> Part one</text><text x="32" y="64"><tspan fill="#f4a32b">■</tspan> Part two</text><text x="54" y="64"><tspan fill="#1fa89a">■</tspan> Part three</text><text x="78" y="64"><tspan fill="#1d4f8c">■</tspan> Part four</text>
    </g>
  </svg>
  <footer class="slide-foot"><span>© 2013 Velmoxa. All rights reserved</span><span>3</span></footer>
</section>

<section class="slide content c3 r4">
  <p class="slide-head">Velmoxa presentation/powerful mission 1</p>
  <div class="brand-mark"><span class="square"></span><span class="name">Velmoxa</span></div>
  <div class="copy abs" style="left:34px;top:58px;width:86px">
    <p>Velmoxa has built a bold and dynamic approach to brand audit and strategy. By clearing old habits, the team has pushed clients to a new level.</p>
    <p>Central to this approach are fresh habits that held the market back. Velmoxa has pushed each project to a new level with new work in audit and strategy. Our partners grow across web and offline channels.</p>
  </div>
  <svg class="abs" style="left:138px;top:70px" width="110" height="92" viewBox="0 0 110 92">
    <rect x="4" y="56" width="12" height="22" fill="#8d8d8d"/><path d="M4 56 L8 52 L20 52 L16 56 Z" fill="#b5b5b5"/><path d="M16 56 L20 52 L20 74 L16 78 Z" fill="#6d6d6d"/>
    <rect x="22" y="62" width="12" height="16" fill="#e8603c"/><path d="M22 62 L26 58 L38 58 L34 62 Z" fill="#f38b6a"/><path d="M34 62 L38 58 L38 74 L34 78 Z" fill="#b84425"/>
    <rect x="40" y="40" width="12" height="38" fill="#f4a32b"/><path d="M40 40 L44 36 L56 36 L52 40 Z" fill="#f8c46e"/><path d="M52 40 L56 36 L56 74 L52 78 Z" fill="#c47d14"/>
    <rect x="58" y="28" width="12" height="50" fill="#1fa89a"/><path d="M58 28 L62 24 L74 24 L70 28 Z" fill="#5ccabd"/><path d="M70 28 L74 24 L74 74 L70 78 Z" fill="#137a70"/>
    <rect x="76" y="12" width="12" height="66" fill="#2a8ad4"/><path d="M76 12 L80 8 L92 8 L88 12 Z" fill="#6cc3f2"/><path d="M88 12 L92 8 L92 74 L88 78 Z" fill="#1f6aa8"/>
    <g font-family="Open Sans, sans-serif" font-size="2.4" fill="#666">
      <text x="4" y="86">Item 1</text><text x="24" y="86">Item 2</text><text x="44" y="86">Item 3</text><text x="64" y="86">Item 4</text><text x="84" y="86">Item 5</text>
    </g>
  </svg>
  <footer class="slide-foot"><span>© 2013 Velmoxa. All rights reserved</span><span>3</span></footer>
</section>

<section class="slide content c4 r4">
  <p class="slide-head">Velmoxa presentation/powerful mission 1</p>
  <div class="brand-mark"><span class="square"></span><span class="name">Velmoxa</span></div>
  <div class="copy abs" style="left:34px;top:58px;width:88px">
    <p>Velmoxa has built a bold and dynamic approach to brand audit and strategy. By clearing old habits, the team has pushed clients to a new level.</p>
    <p>Central to this approach are fresh habits that held the market back. Velmoxa has pushed each project to a new level with new work in audit and strategy. Our partners grow across web and offline channels.</p>
  </div>
  <table class="data abs" style="left:132px;top:62px;width:118px">
    <tr><th>No.</th><th>Name</th><th>Date</th><th>Case</th></tr>
    <tr><td>01.</td><td>Mrs Anna Petrova</td><td>17-06-13</td><td>Open</td></tr>
    <tr><td>02.</td><td>Mrs Irina Lebed</td><td>17-06-13</td><td>Open</td></tr>
    <tr><td>03.</td><td>Mrs Anna Petrova</td><td>17-06-13</td><td>Close</td></tr>
    <tr><td>04.</td><td>Mrs Irina Lebed</td><td>17-06-13</td><td>Open</td></tr>
    <tr><td>05.</td><td>Mrs Anna Petrova</td><td>17-06-13</td><td>Close</td></tr>
    <tr><td>06.</td><td>Mrs Irina Lebed</td><td>17-06-13</td><td>Open</td></tr>
    <tr><td>07.</td><td>Mrs Anna Petrova</td><td>17-06-13</td><td>Close</td></tr>
    <tr><td>08.</td><td>Mrs Irina Lebed</td><td>17-06-13</td><td>Open</td></tr>
  </table>
  <footer class="slide-foot"><span>© 2013 Velmoxa. All rights reserved</span><span>3</span></footer>
</section>

<section class="slide content c1 r5">
  <p class="slide-head">Velmoxa presentation/powerful mission 1</p>
  <div class="brand-mark"><span class="square"></span><span class="name">Velmoxa</span></div>
  <table class="data abs" style="left:36px;top:64px;width:208px">
    <tr><th>No</th><th>Name</th><th>Id Case</th><th>Address</th><th>Date</th><th>Case</th></tr>
    <tr><td>01.</td><td>Mrs Anna Petrova</td><td>621006</td><td>Birch Street 12a</td><td>17-06-13</td><td>Open</td></tr>
    <tr><td>02.</td><td>Mrs Irina Lebed</td><td>621006</td><td>Lake Street 14a</td><td>17-06-13</td><td>Open</td></tr>
    <tr><td>03.</td><td>Mrs Anna Petrova</td><td>621006</td><td>Garden Street 15a</td><td>17-06-13</td><td>Close</td></tr>
    <tr><td>04.</td><td>Mrs Irina Lebed</td><td>621006</td><td>River Street 17a</td><td>17-06-13</td><td>Close</td></tr>
    <tr><td>05.</td><td>Mrs Anna Petrova</td><td>621006</td><td>Birch Street 12a</td><td>17-06-13</td><td>Close</td></tr>
  </table>
  <div class="copy abs" style="left:36px;top:128px;width:208px">
    <p>Velmoxa has built a bold and dynamic approach to brand audit and strategy. By clearing old habits that held the market back, the team has pushed clients to a new level.</p>
    <p>Central to this approach are fresh habits that held the market back. Velmoxa has pushed each project to a new level with new work.</p>
  </div>
  <footer class="slide-foot"><span>© 2013 Velmoxa. All rights reserved</span><span>3</span></footer>
</section>

<section class="slide title-slide c2 r5">
  <div class="backdrop" role="img" aria-label="Faded city bridge backdrop"></div>
  <div class="lower-band"></div>
  <div class="light-brand"><span class="square"></span><span class="name">Velmoxa</span></div>
  <h2 class="big-title" style="top:100px">THANK YOU</h2>
  <p class="sub-title" style="top:122px">YOUR PRESENTATION SUB TITLE HERE</p>
  <p class="light-foot">© 2013 VELMOXA. All rights reserved</p>
</section>

</body>
</html>
```